Step and Repeat Backdrop for wedding reception photo booth

Would like to have a Step and Repeat Backdrop (8 foot high by 10 foot wide) that incorporates the wedding logo (attached) and the names Elena and Gavin. Background should be white, and wedding colors are burgundy and gold. Show me creativity :-) I have included some random samples.

```html
<!DOCTYPE html>
<html lang="en">
<head>
<meta charset="utf-8">
<title>Elena &amp; Gavin — Step and Repeat Backdrop</title>
<link href="https://fonts.googleapis.com/css2?family=Cinzel:wght@500&display=swap" rel="stylesheet">
<style>
  :root {
    --stage: #ececec;
    --panel: #ffffff;
    --gold: #c9a13b;
    --shadow: rgba(0, 0, 0, 0.18);
  }
  * { box-sizing: border-box; margin: 0; padding: 0; }
  html, body {
    width: 1200px;
    height: 900px;
    overflow: hidden;
    background: var(--stage);
  }
  .backdrop {
    position: absolute;
    left: 100px;
    top: 50px;
    width: 1000px;
    height: 800px;
    background: var(--panel);
    box-shadow: 0 4px 14px var(--shadow);
    display: grid;
    grid-template-columns: repeat(6, 160px);
    grid-template-rows: repeat(5, 149px);
    padding: 26px 0 0 20px;
    justify-items: center;
    align-items: center;
  }
  .name-seal {
    width: 130px;
    height: 130px;
    border: 1.5px solid var(--gold);
    border-radius: 50%;
    display: flex;
    align-items: center;
    justify-content: center;
    text-align: center;
    font-family: "Cinzel", serif;
    font-weight: 500;
    color: var(--gold);
    font-size: 17px;
    line-height: 1.25;
    letter-spacing: 0.04em;
  }
  .name-seal--feature {
    grid-column: 3 / 5;
    grid-row: 2 / 4;
    width: 296px;
    height: 296px;
    border-width: 3px;
    font-size: 40px;
  }
</style>
</head>
<body>
  <main class="backdrop" aria-label="Step and repeat backdrop for Elena and Gavin">
    <div class="name-seal name-seal--feature">Elena<br>&amp;<br>Gavin</div>

    <div class="name-seal">Elena<br>&amp; Gavin</div>
    <div class="name-seal">Elena<br>&amp; Gavin</div>
    <div class="name-seal">Elena<br>&amp; Gavin</div>
    <div class="name-seal">Elena<br>&amp; Gavin</div>
    <div class="name-seal">Elena<br>&amp; Gavin</div>
    <div class="name-seal">Elena<br>&amp; Gavin</div>

    <div class="name-seal">Elena<br>&amp; Gavin</div>
    <div class="name-seal">Elena<br>&amp; Gavin</div>
    <div class="name-seal">Elena<br>&amp; Gavin</div>
    <div class="name-seal">Elena<br>&amp; Gavin</div>

    <div class="name-seal">Elena<br>&amp; Gavin</div>
    <div class="name-seal">Elena<br>&amp; Gavin</div>
    <div class="name-seal">Elena<br>&amp; Gavin</div>
    <div class="name-seal">Elena<br>&amp; Gavin</div>

    <div class="name-seal">Elena<br>&amp; Gavin</div>
    <div class="name-seal">Elena<br>&amp; Gavin</div>
    <div class="name-seal">Elena<br>&amp; Gavin</div>
    <div class="name-seal">Elena<br>&amp; Gavin</div>
    <div class="name-seal">Elena<br>&amp; Gavin</div>
    <div class="name-seal">Elena<br>&amp; Gavin</div>

    <div class="name-seal">Elena<br>&amp; Gavin</div>
    <div class="name-seal">Elena<br>&amp; Gavin</div>
    <div class="name-seal">Elena<br>&amp; Gavin</div>
    <div class="name-seal">Elena<br>&amp; Gavin</div>
    <div class="name-seal">Elena<br>&amp; Gavin</div>
    <div class="name-seal">Elena<br>&amp; Gavin</div>
  </main>
</body>
</html>
```